Business Card & Stationary Design Project

We are looking for some creative direction for business cards and our stationary.

We are a global logistics firm that has recently changed its name to Marrick Global Logistics and we have a new website due out tomorrow (www.marrick.com.au).

The colours of the company are rich navy tones, I would like to have business cards that fit together to make one picture on the back (possibly an old map of the world??), and the front to be modern contemporary looking.

But I am open to suggestions, so just incorporate our new logo and get going!
Updates

Hi Everyone,

Thank you for all of your designs so far and the time you have put into it.

I have asked many of you for amendments to see if we can get a final product, so with this in mind I am extending the deadline by a few days.

Good luck and thank you once again.

Please message me direct if you need any clarification.

Kind Regards
Colin

Reason: As outlined the extra 3 days is for amendments and changes to the current submissions. Thanks Colin

Industry/Entity Type

Business

```html
<!DOCTYPE html>
<html lang="en">
<head>
<meta charset="utf-8">
<title>Marrick Global Logistics – Business Card</title>
<link rel="stylesheet" href="https://fonts.googleapis.com/css2?family=Questrial&display=swap">
<style>
  :root {
    --navy: #0d2d57;
    --navy-deep: #0a2447;
    --map-tone: #16355f;
    --globe-blue: #2a7fcf;
    --white: #ffffff;
    --stage: #8e8f91;
    --ink-light: #e8eef6;
  }
  * { margin: 0; padding: 0; box-sizing: border-box; }
  html, body {
    width: 1200px; height: 775px; overflow: hidden;
    background: var(--stage);
    font-family: "Questrial", "Century Gothic", sans-serif;
  }
  .card-set {
    position: absolute; inset: 0;
    display: flex; align-items: center; justify-content: center; gap: 40px;
  }
  .card {
    position: relative;
    width: 520px; height: 316px;
    overflow: hidden;
    background: var(--white);
    box-shadow: 0 6px 18px rgba(0,0,0,0.35);
  }
  .card--front { border-radius: 34px 0 0 34px; }
  .card--back  { border-radius: 0 34px 34px 0; }

  /* Front */
  .brand {
    position: absolute; left: 70px; top: 78px;
    display: flex; align-items: center; gap: 18px;
    color: var(--navy);
  }
  .brand__name {
    font-size: 30px; letter-spacing: 6px; line-height: 1.15;
    text-transform: uppercase;
  }
  .brand__name span { display: block; font-size: 14px; letter-spacing: 7px; }
  .brand__mark {
    width: 50px; height: 50px; border-radius: 50%;
    background: var(--globe-blue);
  }
  .contact-band {
    position: absolute; left: 0; right: 0; bottom: 0; height: 126px;
    background: var(--navy);
    padding: 30px 0 0 70px;
  }
  .contact-list { list-style: none; color: var(--ink-light); font-size: 14.5px; }
  .contact-list li { display: flex; align-items: center; gap: 8px; height: 22px; }
  .contact-list svg { width: 13px; height: 13px; fill: var(--ink-light); flex: none; }

  /* Back */
  .world-map {
    position: absolute; left: 0; right: 0; top: 0; height: 250px;
    background: radial-gradient(ellipse at 55% 45%, var(--map-tone), var(--navy-deep) 75%);
  }
  .web-strip {
    position: absolute; left: 0; right: 0; bottom: 0; height: 66px;
    display: flex; align-items: center; gap: 14px; padding: 0 10px;
    color: var(--navy); font-size: 15px;
  }
  .web-strip::before, .web-strip::after {
    content: ""; flex: 1; height: 1.5px; background: var(--navy);
  }
</style>
</head>
<body>
  <main class="card-set">
    <section class="card card--front" aria-label="Business card front">
      <div class="brand">
        <div class="brand__name">Marrick<span>Global Logistics</span></div>
        <div class="brand__mark" aria-hidden="true"></div>
      </div>
      <div class="contact-band">
        <ul class="contact-list">
          <li>
            <svg viewBox="0 0 16 16" aria-hidden="true"><path d="M8 1 1 7.5h2V15h4v-4h2v4h4V7.5h2z"/></svg>
            : 58 Harbour Lane Millers Point NSW 2000
          </li>
          <li>
            <svg viewBox="0 0 16 16" aria-hidden="true"><path d="M1 3h14v10H1zM2 4.2v.6l6 4.2 6-4.2v-.6z" fill-rule="evenodd"/></svg>
            : info@marrick.com.au
          </li>
          <li>
            <svg viewBox="0 0 16 16" aria-hidden="true"><path d="M4.5 1h7a1 1 0 0 1 1 1v12a1 1 0 0 1-1 1h-7a1 1 0 0 1-1-1V2a1 1 0 0 1 1-1zm.5 2v8h6V3z" fill-rule="evenodd"/></svg>
            : +61-2-8000-4120
          </li>
        </ul>
      </div>
    </section>

    <section class="card card--back" aria-label="Business card back">
      <div class="world-map" role="img" aria-label="Faint navy world map covering the back of the card"></div>
      <div class="web-strip">www.marrick.com.au</div>
    </section>
  </main>
</body>
</html>
```